MOLT - Monitoring Natural Hazards from Space Web Application

KORVEN Sarl is a Luxembourg based Space-Startup that works in the field of Earth Observation. KORVEN is a platform able to extract value-added information from satellite data and is specialized in mapping Natural Disaster (floods, fires etc).

We are now developing a new vertical tool, called MOLT, dedicated to the monitoring of natural hazards in Humanitarian Camps around the world.

The goal of MOLT is to hide to the users' all the complexity of the Satellite Image processing and just provide them the results.

This project require to Design 4 pages of MOLT:
• Public Home Page (Code - V01)
• Dashboard (private Home Page) (Code - V03)
• Monitor (web GIS) (Code - V14)
• Registration Page (Code - V04)

We would like to provide the required time to make a good job.

Target Market(s)

Humanitarian Agencies, Goverments

Coding

Coded - Design and coding required

Number of Pages Required

4 page

Font styles to use
Other font styles liked:
• see the manual attached

Requirements
Must have
• 4 pages. One Home, one form, one dashboard and one web map.
Nice to have
• Please read the attachment with all the detailed instructions

```html
<!DOCTYPE html>
<html lang="en">
<head>
<meta charset="utf-8">
<title>MOLT – Registration</title>
<link rel="stylesheet" href="https://fonts.googleapis.com/css2?family=Jost:wght@400;500;600&family=Space+Mono:wght@400;700&display=swap">
<style>
  :root {
    --page-bg: #f4f5f6;
    --panel: #294d5a;
    --accent: #f0b73a;
    --white: #ffffff;
    --field-text: #8a9196;
    --help: #6f8790;
  }
  * { box-sizing: border-box; margin: 0; padding: 0; }
  html, body { width: 1200px; height: 742px; overflow: hidden; }
  body { background: var(--page-bg); font-family: "Jost", sans-serif; position: relative; }
  .page { position: absolute; left: 57px; top: 57px; width: 1087px; height: 628px; background: var(--panel); }
  .brand { position: absolute; left: 45px; top: 29px; display: flex; align-items: center; gap: 10px; }
  .brand-dot { width: 30px; height: 30px; border: 1.5px solid var(--accent); border-radius: 50%; }
  .brand-name { font-family: "Jost", sans-serif; font-weight: 400; font-size: 22px; letter-spacing: 4px; color: var(--white); }
  .nav { position: absolute; top: 35px; font-family: "Space Mono", monospace; font-size: 11.5px; color: var(--white); }
  .headline { position: absolute; left: 132px; top: 104px; font-family: "Space Mono", monospace; font-weight: 700; font-size: 31px; line-height: 38px; color: var(--white); }
  .intro { position: absolute; left: 374px; top: 106px; width: 170px; font-size: 8px; line-height: 16px; color: var(--white); }
  .intro a, .agree a { color: var(--accent); font-weight: 600; text-decoration: none; }
  .login-link { position: absolute; right: 126px; top: 91px; font-size: 8px; color: var(--accent); display: flex; align-items: center; gap: 6px; }
  .field { position: absolute; }
  .field-label { display: flex; justify-content: space-between; align-items: center; height: 12px; font-size: 8px; color: var(--accent); font-weight: 500; }
  .help { width: 9px; height: 9px; border-radius: 50%; background: var(--help); color: var(--panel); font-size: 6px; font-weight: 600; display: flex; align-items: center; justify-content: center; }
  .input { margin-top: 3px; height: 27px; background: var(--white); font-size: 8px; color: var(--field-text); display: flex; align-items: center; justify-content: space-between; padding: 0 9px; }
  .address { position: absolute; left: 619px; top: 355px; width: 355px; height: 173px; border: 1px solid var(--accent); border-radius: 3px; }
  .address-title { position: absolute; left: 6px; top: -7px; padding: 0 6px; background: var(--panel); font-size: 10px; color: var(--accent); line-height: 13px; }
  .agree { position: absolute; left: 619px; display: flex; align-items: center; gap: 9px; font-size: 8px; color: var(--white); }
  .checkbox { width: 9px; height: 9px; background: var(--white); }
  .register { position: absolute; left: 887px; top: 555px; width: 89px; height: 32px; border-radius: 16px; background: var(--accent); color: var(--white); font-size: 10px; font-weight: 600; display: flex; align-items: center; justify-content: center; }
</style>
</head>
<body>
<main class="page">
  <div class="brand"><span class="brand-dot"></span><span class="brand-name">MOLT</span></div>
  <span class="nav" style="left:415px">Home</span>
  <span class="nav" style="left:494px">Features</span>
  <span class="nav" style="left:601px">Pricing</span>

  <h1 class="headline">Input your<br>information</h1>
  <p class="intro">We need you to help us with some basic information for your account creation. Here are our <a href="#">terms and conditions</a>. Please read them carefully.</p>

  <div class="login-link">Allready have an account?
    <svg width="9" height="9" viewBox="0 0 10 10"><circle cx="5" cy="3" r="2.4" fill="#f0b73a"/><path d="M0.5 10c0-3 2-4.5 4.5-4.5S9.5 7 9.5 10z" fill="#f0b73a"/></svg>
  </div>

  <!-- Account details -->
  <div class="field" style="left:134px;top:199px;width:355px"><div class="field-label">User ID<span class="help">?</span></div><div class="input">Insert User ID</div></div>
  <div class="field" style="left:134px;top:256px;width:355px"><div class="field-label">Password<span class="help">?</span></div><div class="input">Insert Password</div></div>
  <div class="field" style="left:134px;top:312px;width:355px"><div class="field-label">Confirm Password<span class="help">?</span></div><div class="input">Insert Password Confirmation</div></div>
  <div class="field" style="left:134px;top:369px;width:355px"><div class="field-label">Name<span class="help">?</span></div><div class="input">Insert Fullname</div></div>
  <div class="field" style="left:134px;top:425px;width:355px"><div class="field-label">Surname<span class="help">?</span></div><div class="input">Insert Surname</div></div>
  <div class="field" style="left:134px;top:482px;width:355px"><div class="field-label">Mobile Phone Number<span class="help">?</span></div><div class="input">Insert Mobile Phone Number</div></div>

  <!-- Organization details -->
  <div class="field" style="left:619px;top:120px;width:355px"><div class="field-label">E-Mail<span class="help">?</span></div><div class="input">Insert E-Mail</div></div>
  <div class="field" style="left:619px;top:176px;width:355px"><div class="field-label">Cofirm E-Mail<span class="help">?</span></div><div class="input">Insert E-Mail Confirmation</div></div>
  <div class="field" style="left:619px;top:233px;width:355px"><div class="field-label">Organization Name<span class="help">?</span></div><div class="input">Insert Organization Name</div></div>
  <div class="field" style="left:619px;top:290px;width:355px"><div class="field-label">Organization Type<span class="help">?</span></div><div class="input">Select<svg width="9" height="6" viewBox="0 0 9 6"><path d="M0.5 0.5 4.5 5 8.5 0.5" fill="none" stroke="#6b7378" stroke-width="1"/></svg></div></div>

  <fieldset class="address">
    <span class="address-title">Organization Address</span>
  </fieldset>
  <div class="field" style="left:631px;top:370px;width:160px"><div class="field-label">Street<span class="help">?</span></div><div class="input">Insert Street</div></div>
  <div class="field" style="left:807px;top:370px;width:160px"><div class="field-label">N.<span class="help">?</span></div><div class="input">Insert N.</div></div>
  <div class="field" style="left:631px;top:420px;width:160px"><div class="field-label">Postal Code<span class="help">?</span></div><div class="input">Insert Postal Code</div></div>
  <div class="field" style="left:807px;top:420px;width:160px"><div class="field-label">City<span class="help">?</span></div><div class="input">Insert City</div></div>
  <div class="field" style="left:631px;top:471px;width:160px"><div class="field-label">Phone<span class="help">?</span></div><div class="input">Insert Postal Code</div></div>
  <div class="field" style="left:807px;top:471px;width:160px"><div class="field-label">Country<span class="help">?</span></div><div class="input">Select Country<svg width="9" height="6" viewBox="0 0 9 6"><path d="M0.5 0.5 4.5 5 8.5 0.5" fill="none" stroke="#6b7378" stroke-width="1"/></svg></div></div>

  <label class="agree" style="top:554px"><span class="checkbox"></span>I have read and Accept the MOLT <a href="#">Terms and Conditins</a>.</label>
  <label class="agree" style="top:572px"><span class="checkbox"></span>I have read and Accept the MOLT <a href="#">Privacy Policy</a>.</label>

  <div class="register">Register</div>
</main>
</body>
</html>
```